HotSite for a 3-day Conference (To build in 24hs)

We need a hot-site for our 3-Day Conference before next Wednesday 17/Jan.

How is it now:
Today all information about our conference is shown in 1 simple page inside our website: https://www.qivbeltanorth.com/grand-lodging-forum.

What we need:
A hot-site focused on our conference where people can see all information about the event, buy tickets and pay it on-line.

The visual:
Luxury, minimalist menu, big full screen light video backgrounds.

Index:
Full animated/light video image and:
Grand Lodging Forum® Paris - 2024
1, 2 and 3rd November
Hotel La Rive Dorée
REGISTER NOW

MENU
I want a double layer/line top menu:

- First menu line (smaller, not the most important/relevant)
- Second menu line (main menu)

First menu line:
About us
Conferences
Newsroom
Careers
Become a Sponsor

The main menu items are:
AGENDA
SPEAKERS
SPONSORS
PREVIOUS EDITIONS
ATTEND/REGISTER NOW

Some references:
https://opulentworld.live.kx.com
https://pivotra.us/conference
https://www.holvenix.com/en/conferences

Coding

Coded - Design and coding required

```html
<!DOCTYPE html>
<html lang="en">
<head>
<meta charset="utf-8">
<title>Grand Lodging Forum® — Qivbelta North</title>
<link rel="stylesheet" href="https://fonts.googleapis.com/css2?family=Playfair+Display:wght@400;500&family=Poppins:wght@400;500;600&display=swap">
<style>
:root{
  --gold:#c9a85c;
  --gold-light:#d9bb74;
  --gold-band:#cdae66;
  --gold-card:#b8903a;
  --ink:#2a2a2a;
  --dark:#2b2b2b;
  --footer:#151515;
  --white:#ffffff;
  --tuition-box:#b2a899;
  --line:#ecd9b0;
}
*{box-sizing:border-box;margin:0;padding:0}
html,body{width:1200px;height:4677px;overflow:hidden;background:var(--white)}
body{font-family:"Poppins",sans-serif;color:var(--ink);position:relative}
h1,h2,h3,h4{font-weight:400}
section,header,footer{position:absolute;left:0;width:1200px}

/* Hero */
.hero{top:0;height:733px;overflow:hidden}
.hero-media{position:absolute;inset:0;background:linear-gradient(180deg,#7e8a98 0%,#8d857a 40%,#7a6a55 70%,#3f4a38 100%)}
.hero-shade{position:absolute;inset:0;background:rgba(40,30,20,.25)}
.brand{position:absolute;left:110px;top:18px;color:var(--gold);font-family:"Playfair Display",serif;font-weight:400;font-size:34px;line-height:1.1;width:220px}
.brand span{display:block;font-family:"Poppins",sans-serif;font-size:13px;letter-spacing:4px;margin-top:10px}
.nav-top{position:absolute;right:112px;top:14px;display:flex;gap:36px;font-size:12px;color:var(--white)}
.nav-main{position:absolute;left:394px;top:52px;width:695px;height:36px;background:var(--gold-light);display:flex;justify-content:space-around;align-items:center;font-size:12.5px;color:var(--white);padding:0 14px}
.hero-title{position:absolute;top:282px;width:100%;text-align:center;font-family:"Playfair Display",serif;font-weight:400;font-size:58px;color:var(--white)}
.hero-title em{font-style:normal;color:var(--gold-light)}
.play{position:absolute;left:530px;top:384px;display:flex;align-items:center;gap:10px;color:var(--white);font-size:15px}
.play .label{border-bottom:1px solid var(--white)}

/* Content */
.content{top:733px;height:577px}
.section-title{text-align:center;font-family:"Playfair Display",serif;font-weight:400;font-size:30px;color:var(--ink)}
.section-title em{font-style:normal;color:var(--gold)}
.content .section-title{position:absolute;top:75px;width:100%}
.topics{position:absolute;left:198px;top:150px;display:grid;grid-template-columns:477px 332px;list-style:none}
.topics li{height:74px;padding-top:8px;font-size:16px;white-space:nowrap;position:relative}
.topics li:after{content:"";position:absolute;left:0;top:52px;width:332px;height:3px;background:var(--line)}

/* Paris band */
.event{top:1310px;height:893px;background:var(--gold-band);text-align:center;color:var(--ink)}
.event h2{font-family:"Playfair Display",serif;font-size:30px;padding-top:70px}
.event .date{font-family:"Playfair Display",serif;font-size:21px;margin-top:6px}
.event p{font-size:14.5px;line-height:25px;width:720px;margin:14px auto 0}
.tiles{position:absolute;top:353px;left:200px;display:flex;gap:40px}
.tile{width:380px;height:378px;border:6px solid #111;position:relative}
.tile .fill{position:absolute;inset:0}
.tile .word{position:absolute;top:20px;width:100%;text-align:center;font-family:"Playfair Display",serif;font-size:34px;letter-spacing:20px;color:var(--white)}
.btn{display:inline-flex;align-items:center;gap:10px;background:var(--gold);color:var(--ink);font-family:"Playfair Display",serif;font-size:14px;padding:10px 12px 10px 22px;border-radius:24px}
.event .btn{position:absolute;top:762px;left:514px}
.btn i{width:20px;height:20px;border-radius:50%;background:var(--white);display:inline-block;position:relative}
.btn i:after{content:"";position:absolute;left:8px;top:6px;border-left:6px solid var(--ink);border-top:4px solid transparent;border-bottom:4px solid transparent}

/* Speakers */
.speakers{top:2203px;height:804px}
.speakers .section-title{position:absolute;top:70px;width:100%;font-size:34px}
.speaker{position:absolute;width:230px;height:270px;border:4px solid var(--gold-light);border-radius:12px;overflow:hidden;box-shadow:0 6px 14px rgba(0,0,0,.25);color:var(--white);text-align:center}
.speaker .photo{position:absolute;inset:0;background:linear-gradient(180deg,#9a9a9a 0%,#5a5148 60%,#2a241d 100%)}
.speaker .info{position:absolute;bottom:6px;width:100%;padding:0 4px}
.speaker b{display:block;font-weight:600;font-size:18px}
.speaker small{display:block;font-size:13px;line-height:17px}

/* Tuition */
.tuition{top:3007px;height:423px;background:var(--dark);color:var(--white)}
.tuition h3{position:absolute;top:72px;font-family:"Playfair Display",serif;font-size:30px}
.tuition h3:after{content:"";position:absolute;left:0;bottom:-10px;width:44px;height:3px;background:var(--gold)}
.price{position:absolute;top:128px;width:186px;height:138px;background:var(--tuition-box);font-family:"Playfair Display",serif;padding:14px 16px}
.price .t{font-size:18px}
.price .d{font-size:11px}
.price .v{font-size:29px;margin-top:28px}
.notes{position:absolute;left:112px;top:303px;font-family:"Playfair Display",serif;font-size:12px;line-height:25px}

/* Schedule */
.schedule{top:3430px;height:916px}
.schedule .section-title{position:absolute;top:78px;width:100%;font-size:34px}
.day{position:absolute;top:144px;width:325px;height:686px;background:var(--gold-card);border-radius:14px;overflow:hidden;color:var(--white)}
.day h4{background:var(--gold-light);height:62px;padding-top:20px;text-align:center;font-family:"Playfair Display",serif;font-size:18px;color:var(--ink)}
.day ul{list-style:none;padding:0 18px 0 26px}
.day li{font-size:12.5px;line-height:17px;padding:12px 0 10px;border-bottom:1px solid rgba(255,255,255,.35)}

/* Footer */
.site-footer{top:4346px;height:331px;background:var(--footer);color:var(--white);text-align:center}
.site-footer .brand{position:static;margin:60px auto 0;width:auto;text-align:center}
.foot-nav{display:flex;justify-content:center;gap:36px;font-size:13px;font-weight:500;margin-top:50px}
.foot-rule{position:absolute;left:110px;right:110px;top:258px;border-top:1px solid #444}
.copy{position:absolute;top:288px;width:100%;font-size:12px}
</style>
</head>
<body>

<header class="hero">
  <div class="hero-media" role="img" aria-label="Grand historic hotel with a central tower framed by palm trees under a soft sky"></div>
  <div class="hero-shade"></div>
  <div class="brand">Qivbelta North<span>PARIS FORUMS</span></div>
  <nav class="nav-top"><span>ABOUT US</span><span>CONFERENCES</span><span>NEWSROOM</span><span>CAREERS</span><span>BECOME A SPONSOR</span></nav>
  <nav class="nav-main"><span>AGENDA</span><span>SPEAKERS</span><span>SPONSORS</span><span>PREVIOUS EDITIONS</span><span>ATTEND/REGISTER NOW</span></nav>
  <h1 class="hero-title"><em>Grand Lodging</em> Forum®</h1>
  <div class="play">
    <svg width="44" height="44" viewBox="0 0 44 44"><circle cx="22" cy="22" r="21" fill="#fff"/><path d="M17 13 L31 22 L17 31Z" fill="#c9a85c"/></svg>
    <span class="label">Play Video</span>
  </div>
</header>

<section class="content">
  <h2 class="section-title">Content</h2>
  <ul class="topics">
    <li>The Luxury Traveller's Evolution Over Time</li><li>Luxury Consumer Behavior</li>
    <li>New Distribution Channels in Luxury Hospitality</li><li>Luxury Brand Management</li>
    <li>Innovation in Luxury Hospitality</li><li>Luxury Boutique Hotel Strategies</li>
    <li>How to Maintain Luxury in Large Scale Operations</li><li>Generating Unique Experiences</li>
    <li>Luxury Hotel Chain Management</li><li>Forming Strategic Alliances</li>
  </ul>
</section>

<section class="event">
  <h2>Paris</h2>
  <div class="date">November 1-3, 2024</div>
  <p>The ever-growing Luxury Hospitality business is one of the most exciting industries in the world.</p>
  <p>At our Grand Lodging Forum, top figures in the industry share their experiences and give unique insights, speaking about challenges, entrepreneurial management, vision and prospects for the future.</p>
  <p>The forum leads directly into Hostexpo, the most important Hospitality event in the world.</p>
  <div class="tiles">
    <div class="tile"><div class="fill" role="img" aria-label="Bright modern hotel lounge with white sofas and teal accents" style="background:linear-gradient(160deg,#e8e6e2,#b9b3aa 60%,#6d6258)"></div><div class="word">DESIGN</div></div>
    <div class="tile"><div class="fill" role="img" aria-label="City skyline with a tall tower above the water at dusk" style="background:linear-gradient(180deg,#6f7a88,#3e4656 60%,#232a36)"></div><div class="word">CHANGE</div></div>
  </div>
  <a class="btn">REGISTER NOW <i></i></a>
</section>

<section class="speakers">
  <h2 class="section-title"><em>Speaker</em> Line-Up</h2>
  <div class="speaker" style="left:112px;top:149px"><div class="photo" role="img" aria-label="Portrait of Marco Vellani"></div><div class="info"><b>Marco Vellani</b><small>President of QIV</small></div></div>
  <div class="speaker" style="left:360px;top:149px"><div class="photo" role="img" aria-label="Portrait of Jean-Paul Ravier"></div><div class="info"><b>Jean-Paul Ravier</b><small>CEO, La Quiétude</small></div></div>
  <div class="speaker" style="left:609px;top:149px"><div class="photo" role="img" aria-label="Portrait of Pieter Daelmans" style="background:linear-gradient(180deg,#5d7a4c,#4a5040 60%,#2a2a2a)"></div><div class="info"><b>Pieter Daelmans</b><small>CEO, Petite Grand Hotels<br>of the World</small></div></div>
  <div class="speaker" style="left:857px;top:149px"><div class="photo" role="img" aria-label="Portrait of Adrian Holtberg" style="background:linear-gradient(180deg,#c9c6c0,#8a8580 60%,#3a3836)"></div><div class="info"><b>Adrian Holtberg</b><small>General Director, Hotel Solenne Paris</small></div></div>
  <div class="speaker" style="left:237px;top:445px"><div class="photo" role="img" aria-label="Portrait of Luca Ferrandi" style="background:linear-gradient(180deg,#b8863a,#7a5a30 60%,#2f2418)"></div><div class="info"><b>Luca Ferrandi</b><small>Former VP, Sandpalm Resorts</small></div></div>
  <div class="speaker" style="left:485px;top:445px"><div class="photo" role="img" aria-label="Portrait of Étienne Marchetti" style="background:linear-gradient(180deg,#d8d2c6,#9a8f80 60%,#3c352e)"></div><div class="info"><b>Étienne Marchetti</b><small>COO, Westbury Collection</small></div></div>
  <div class="speaker" style="left:734px;top:445px"><div class="photo" role="img" aria-label="Portrait of Henri Castelmont" style="background:linear-gradient(180deg,#c49a4a,#8a6a3c 60%,#3a2c1c)"></div><div class="info"><b>Henri Castelmont</b><small>Former Executive VP,<br>Maison Orvel (23 years)</small></div></div>
</section>

<section class="tuition">
  <h3 style="left:110px">Tuition</h3>
  <div class="price" style="left:110px"><div class="t">Early birds</div><div class="d">until 08/30/2024</div><div class="v">€3.750,00</div></div>
  <div class="price" style="left:308px"><div class="t">After</div><div class="d">08/30/2024</div><div class="v">€5.000,00</div></div>
  <h3 style="left:705px">QIV Students</h3>
  <div class="price" style="left:706px"><div class="t">Early birds</div><div class="d">until 08/30/2024</div><div class="v">€3.000,00</div></div>
  <div class="price" style="left:904px"><div class="t">After</div><div class="d">08/30/2024</div><div class="v">€3.500,00</div></div>
  <div class="notes">* &nbsp;Discounts available for groups and partner Universities<br>* &nbsp;Lodging and meals not included</div>
</section>

<section class="schedule">
  <h2 class="section-title"><em>Daily</em> Schedule</h2>
  <article class="day" style="left:93px">
    <h4>Nov. 1 - Tradition vs. Innovation</h4>
    <ul>
      <li>09:00 - Official Opening<br>Marco Vellani | QIV</li>
      <li>09:15 - The Legend is Back<br>Adrian Holtberg | Solenne Paris</li>
      <li>10:30 - Coffee Break</li>
      <li>11:00 - The Luxury Traveller's Evolution Over Time<br>Adrian Holtberg | Solenne Paris</li>
      <li>12:00 - Lunch</li>
      <li>14:00 - Luxury Consumer Behavior<br>Henri Castelmont | Maison Orvel (23 years)</li>
      <li>15:30 - Coffee Break</li>
      <li>16:00 - Roads to Luxury<br>Henri Castelmont | Maison Orvel (23 years)</li>
      <li>17:00 - Closure</li>
      <li>19:30 - Social Program - Pâtisserie<br>Class at École Maréchal</li>
    </ul>
  </article>
  <article class="day" style="left:437px">
    <h4>Nov. 2 - The Era of Experiences</h4>
    <ul>
      <li>09:00 - Luxury Boutique Hotel Strategies<br>Jean-Paul Ravier | La Quiétude</li>
      <li>10:30 - Coffee Break</li>
      <li>11:00 - Generating Unique Experiences<br>Jean-Paul Ravier | La Quiétude</li>
      <li>12:00 - Lunch</li>
      <li>14:00 - Smaller is Greater<br>Pieter Daelmans | Petite Grand Hotels of the World</li>
      <li>15:30 - Coffee Break</li>
      <li>16:00 - Site Inspection -<br>Spa Hotel La Quiétude</li>
      <li>17:00 - Closure</li>
      <li>17:30 - Social Program - Guided<br>Visit to Musée Verlaine</li>
    </ul>
  </article>
  <article class="day" style="left:781px">
    <h4>Nov. 3 - A Glimpse of the Future</h4>
    <ul>
      <li>09:00 - Innovation in Luxury Hospitality<br>Luca Ferrandi | Workbay</li>
      <li>10:30 - Coffee Break</li>
      <li>11:00 - Site Inspection - Hotel Maravel Étoile</li>
      <li>12:00 - Lunch</li>
      <li>14:00 - Luxury Hotel Chain Management<br>Étienne Marchetti | Westbury Collection</li>
      <li>15:30 - Coffee Break</li>
      <li>16:00 - Panel of Discussion -<br>New Competitors</li>
      <li>17:00 - Closure and Certificates</li>
    </ul>
  </article>
</section>

<footer class="site-footer">
  <div class="brand">Qivbelta North<span>PARIS FORUMS</span></div>
  <nav class="foot-nav"><span>AGENDA</span><span>SPEAKERS</span><span>SPONSORS</span><span>PREVIOUS EDITIONS</span><span>ATTEND/REGISTER NOW</span></nav>
  <div class="foot-rule"></div>
  <div class="copy">©2024. All rights reserved.</div>
</footer>

</body>
</html>
```